Lawn Company needs design work on a service call flyer!

We are a lawn care company that fertilizes and sprays lawns. This design is meant to be left behind at the customers house after a lawn application has been done too let them know what we have done.

The finished design will be printed on A6 paper (4.1 x 5.8 inches)

I have attached PDF files of the text that I want on the front of the document and the back of the document. I also included a sample design that I had been working on to give some idea what I would like. I don't want the same design, but you can use it as a building block for something new or come up with something entirely different.

FRONT: The front of the design is most important.

BACK: Other then the text the design should be minimal. If possible I would like an outline of the trees in my logo to be a backdrop. I have attached a PDF of the back of my business card as an example

The winning design will be a professional looking document that flows and reflects a lawn care business. Please contact me if you have any questions. I will only pick a design that is better then my current template.

Thank You

Target Market(s)

Lawn Care Customers

Industry/Entity Type

Lawn Care

Requirements
Must have
• 1. Our Logo
• 2. The attached text for the front & back of document
• 3. Our phone number (604-918-4471)
• 4. Our Email address (fenwickturfcare@mailora.net)
Nice to have
• A green theme with flowing graphics
Should not have
• any pictures of houses, people, or tools
• Don't copy the text or design from my design template. It is outdated, is it meant to be an example only

```html
<!DOCTYPE html>
<html lang="en">
<head>
<meta charset="utf-8">
<title>Fenwick Turf Care – Service Call Notice</title>
<link href="https://fonts.googleapis.com/css2?family=Lato:wght@400;700;900&display=swap" rel="stylesheet">
<style>
  :root {
    --ink: #111111;
    --green-deep: #0b4f2a;
    --green-dark: #126b32;
    --green-mid: #2f9a2c;
    --green-bright: #6cd12a;
    --lime: #c8e63c;
    --paper: #f6f8f3;
    --paper-shade: #e4ebdf;
    --white: #ffffff;
  }
  * { margin: 0; padding: 0; box-sizing: border-box; }
  html, body { width: 1200px; height: 863px; overflow: hidden; background: var(--white); }
  .flyer {
    position: relative;
    width: 1200px;
    height: 863px;
    overflow: hidden;
    font-family: "Lato", sans-serif;
    color: var(--ink);
    background:
      radial-gradient(ellipse at 80% 45%, var(--white), transparent 60%),
      linear-gradient(160deg, var(--paper) 0%, var(--paper-shade) 100%);
  }
  .waves { position: absolute; inset: 0; width: 1200px; height: 863px; }

  .brand {
    position: absolute;
    left: 44px;
    top: 44px;
    display: flex;
    align-items: center;
    gap: 16px;
  }
  .brand-dot {
    width: 22px;
    height: 22px;
    border-radius: 50%;
    background: var(--lime);
  }
  .brand-name {
    font-size: 42px;
    font-weight: 900;
    letter-spacing: 2px;
    color: var(--white);
  }

  .line { position: absolute; white-space: nowrap; font-size: 28px; }
  .app-date { left: 646px; top: 218px; }
  .serviced-by { left: 44px; top: 284px; }
  .intro { left: 44px; top: 350px; }
  .treatment { left: 107px; }
  .t1 { top: 403px; }
  .t2 { top: 451px; }
  .t3 { top: 499px; }
  .watering { left: 44px; top: 581px; }

  .guarantee-title {
    position: absolute;
    left: 43px;
    top: 636px;
    font-size: 34px;
    font-weight: 700;
    letter-spacing: -0.5px;
  }
  .guarantee-text {
    position: absolute;
    left: 43px;
    top: 692px;
    width: 1114px;
    font-size: 24.5px;
    line-height: 30px;
    text-align: justify;
  }

  .contact {
    position: absolute;
    left: 0;
    right: 0;
    bottom: 12px;
    display: flex;
    justify-content: center;
    gap: 70px;
    color: var(--white);
    font-size: 22px;
    font-weight: 700;
    letter-spacing: 0.5px;
  }
  .contact-item { display: flex; align-items: center; gap: 10px; }
  .contact-icon { width: 24px; height: 24px; }
</style>
</head>
<body>
<main class="flyer">
  <svg class="waves" viewBox="0 0 1200 863" aria-hidden="true">
    <defs>
      <linearGradient id="header-fill" x1="0" y1="0" x2="1" y2="0">
        <stop offset="0" stop-color="var(--green-deep)"/>
        <stop offset="0.55" stop-color="var(--green-dark)"/>
        <stop offset="1" stop-color="var(--green-mid)"/>
      </linearGradient>
      <linearGradient id="accent-fill" x1="0" y1="0" x2="1" y2="0">
        <stop offset="0" stop-color="var(--green-bright)"/>
        <stop offset="1" stop-color="var(--lime)"/>
      </linearGradient>
      <linearGradient id="footer-fill" x1="0" y1="0" x2="1" y2="0">
        <stop offset="0" stop-color="var(--green-mid)"/>
        <stop offset="0.5" stop-color="var(--green-dark)"/>
        <stop offset="1" stop-color="var(--green-deep)"/>
      </linearGradient>
    </defs>
    <!-- header: layered flowing waves -->
    <path d="M0 0 H1200 V150 C1050 200 900 120 720 140 C520 162 320 200 0 160 Z" fill="url(#accent-fill)" opacity="0.55"/>
    <path d="M0 0 H1200 V118 C1040 160 880 96 700 112 C500 130 300 170 0 138 Z" fill="url(#accent-fill)"/>
    <path d="M0 0 H1200 V98 C1040 136 880 78 700 92 C500 108 300 148 0 122 Z" fill="url(#header-fill)"/>
    <!-- footer -->
    <path d="M0 808 C300 790 520 818 760 804 C960 792 1100 780 1200 786 V863 H0 Z" fill="url(#accent-fill)"/>
    <path d="M0 818 C300 800 520 828 760 814 C960 802 1100 792 1200 798 V863 H0 Z" fill="url(#footer-fill)"/>
  </svg>

  <div class="brand">
    <span class="brand-dot"></span>
    <span class="brand-name">FENWICK TURF CARE</span>
  </div>

  <p class="line app-date">APPLICATION TIME / DATE:____________</p>
  <p class="line serviced-by">YOUR LAWN HAS BEEN PROFFESIONALLY SERVICED TODAY BY______________________</p>
  <p class="line intro">Today's application consists of</p>
  <p class="line treatment t1">Seasonally Balanced Slow Release Fertilizer</p>
  <p class="line treatment t2">Broadleaf Weed Control (Please keep off the lawn until it is thoroughly dry)</p>
  <p class="line treatment t3">Other _____________</p>
  <p class="line watering">Please begin watering the lawn _________________ after application</p>

  <h2 class="guarantee-title">Our Guarantee</h2>
  <p class="guarantee-text">“We strive to complete work in a professional manner each and every visit. If you are not satisfied with the level of service you are receiving please contact us. We value your business and wish to maintain long-term relationships with our customers.“</p>

  <footer class="contact">
    <span class="contact-item">
      <svg class="contact-icon" viewBox="0 0 24 24" aria-hidden="true"><path fill="#ffffff" d="M6.6 10.8a15.1 15.1 0 0 0 6.6 6.6l2.2-2.2a1 1 0 0 1 1-.25 11.4 11.4 0 0 0 3.6.57 1 1 0 0 1 1 1V20a1 1 0 0 1-1 1A17 17 0 0 1 3 4a1 1 0 0 1 1-1h3.5a1 1 0 0 1 1 1c0 1.25.2 2.45.57 3.57a1 1 0 0 1-.25 1z"/></svg>
      604-918-4471
    </span>
    <span class="contact-item">
      <svg class="contact-icon" viewBox="0 0 24 24" aria-hidden="true"><rect x="2" y="5" width="20" height="14" rx="2" fill="none" stroke="#ffffff" stroke-width="2"/><path d="M3 6l9 7 9-7" fill="none" stroke="#ffffff" stroke-width="2"/></svg>
      fenwickturfcare@mailora.net
    </span>
  </footer>
</main>
</body>
</html>
```